Innovative Freezer Label Design

Create a versatile and innovative freezer label design with universal appeal, suitable for different functionalities. The design should cater to a diverse audience, including those who freeze meals for meal prepping, batch cooking, and the restaurant industry. Our vision is a visually striking and distinctive design that embodies simplicity.

Example "our current labels feature essential details like "Contents" and "Date." We recognize these as crucial points of information. Currently, the challenge lies in creating various labels for different marketplaces, considering language barriers. A proposed solution involves the integration of universal icons to replace specific words, promoting practicality for international sales."

Kindly note that design concepts should not be restricted to our current product, brand guideline, logo, or the provided example.

Our goal is not only product differentiation but also increased sales through a blend of functionality and aesthetics.

The following are examples of freezer labels designs. Kindly do not restrict your designs to the examples. The designs must be universal (for language barrier purposes)

Examples:
https://www.snaprovel.co.uk/pin/5820174630298837415/
https://www.snaprovel.co.uk/pin/5820174630298837419/
https://www.snaprovel.co.uk/pin/5820174630298837408/
https://www.snaprovel.co.uk/pin/5820174630298837322/
https://www.snaprovel.co.uk/pin/5820174630298898764/

Please reach out if you have any questions.

Thank you

```html
<!DOCTYPE html>
<html lang="en">
<head>
<meta charset="UTF-8">
<title>Freezer Label Collection</title>
<link href="https://fonts.googleapis.com/css2?family=Open+Sans:wght@400;600&display=swap" rel="stylesheet">
<style>
  :root {
    --bg-top: #e1e1e0;
    --bg-bottom: #aeb2b4;
    --label-white: #ffffff;
    --label-edge: #9a9c9e;
    --slate-band: #4a5b6e;
    --ink: #3a3f45;
    --dots: #8d9196;

    --copper-1: #b6835f;
    --copper-2: #c9a084;
    --copper-3: #dfc4b2;

    --steel-1: #4f5d6c;
    --steel-2: #6f7e8c;
    --steel-3: #9ba7b2;
    --steel-mark: #3e4a57;

    --teal-1: #1f5571;
    --teal-2: #4f7c91;
    --teal-3: #7fa3b4;
  }
  * { margin: 0; padding: 0; box-sizing: border-box; }
  html, body { width: 819px; height: 1200px; overflow: hidden; }
  body {
    position: relative;
    background: linear-gradient(180deg, var(--bg-top) 0%, #d6d7d7 55%, var(--bg-bottom) 100%);
    font-family: "Open Sans", Arial, sans-serif;
    color: var(--ink);
  }

  .product-photo {
    position: absolute;
    left: 165px; top: 134px;
    width: 486px; height: 576px;
    background:
      linear-gradient(160deg, rgba(90,150,60,0.95) 0%, rgba(120,170,70,0.9) 30%, rgba(210,120,50,0.85) 55%, rgba(40,90,45,0.95) 75%, rgba(235,110,40,0.95) 100%);
  }

  .label {
    position: absolute;
    width: 320px; height: 176px;
    background: var(--label-white);
    border: 1px solid var(--label-edge);
    border-radius: 12px;
    overflow: hidden;
    box-shadow: 0 1px 3px rgba(0,0,0,0.12);
  }

  .icon { display: block; fill: none; stroke-width: 1.6; stroke-linecap: round; stroke-linejoin: round; }

  /* banded label */
  .label--banded { left: 81px; top: 770px; border-color: var(--slate-band); }
  .label--banded .band { position: absolute; left: 0; right: 0; height: 19px; background: var(--slate-band); }
  .label--banded .band--top { top: 0; }
  .label--banded .band--bottom { bottom: 0; }
  .label--banded .field { position: absolute; left: 21px; width: 18px; height: 18px; }
  .label--banded .field .icon { stroke: var(--slate-band); }
  .label--banded .field--contents { top: 34px; }
  .label--banded .field--date { top: 119px; }
  .label--banded .slash { position: absolute; top: 119px; font-size: 13px; line-height: 18px; color: var(--ink); }
  .label--banded .slash--one { left: 118px; }
  .label--banded .slash--two { left: 195px; }

  /* tabbed labels */
  .label--copper { left: 418px; top: 771px; }
  .label--steel  { left: 83px;  top: 964px; }
  .label--teal   { left: 418px; top: 964px; }

  .brand-name {
    position: absolute; left: 30px; top: 14px;
    font-size: 15px; font-weight: 600; letter-spacing: 1px;
  }
  .label--copper .brand-name { color: var(--copper-1); }
  .label--steel .brand-name  { color: var(--steel-mark); }
  .label--teal .brand-name   { color: var(--teal-1); }

  .row { position: absolute; left: 0; right: 0; height: 22px; }
  .row--contents { top: 49px; }
  .row--date { top: 90px; }
  .row--instructions { top: 130px; }
  .tab {
    position: absolute; left: 0; top: 0;
    width: 102px; height: 22px;
    display: flex; align-items: center; justify-content: center;
  }
  .tab .icon { width: 16px; height: 16px; stroke: #fff; }
  .dotted-line {
    position: absolute; left: 106px; right: 14px; top: 11px;
    border-top: 1px dotted var(--dots);
  }

  .label--copper .row--contents .tab { background: var(--copper-1); }
  .label--copper .row--date .tab { background: var(--copper-2); }
  .label--copper .row--instructions .tab { background: var(--copper-3); }
  .label--steel .row--contents .tab { background: var(--steel-1); }
  .label--steel .row--date .tab { background: var(--steel-2); }
  .label--steel .row--instructions .tab { background: var(--steel-3); }
  .label--teal .row--contents .tab { background: var(--teal-1); }
  .label--teal .row--date .tab { background: var(--teal-2); }
  .label--teal .row--instructions .tab { background: var(--teal-3); }
</style>
</head>
<body>

  <svg width="0" height="0" style="position:absolute" aria-hidden="true">
    <defs>
      <symbol id="icon-contents" viewBox="0 0 20 20">
        <path d="M3 8h14l-1.5 8.5h-11z"/>
        <path d="M2 8h16"/>
        <path d="M7 8V5.5a3 3 0 0 1 6 0V8"/>
      </symbol>
      <symbol id="icon-date" viewBox="0 0 20 20">
        <rect x="3" y="4.5" width="14" height="12.5" rx="1.5"/>
        <path d="M3 8.5h14M7 2.5v4M13 2.5v4"/>
      </symbol>
      <symbol id="icon-instructions" viewBox="0 0 20 20">
        <path d="M10 2v16M3.1 6l13.8 8M3.1 14l13.8-8"/>
        <path d="M8 3.5l2 2 2-2M8 16.5l2-2 2 2"/>
      </symbol>
    </defs>
  </svg>

  <div class="product-photo" role="img" aria-label="Freezer bags of peas, mixed vegetables, carrot sticks and green beans on a wooden board, each with a label applied"></div>

  <div class="label label--banded">
    <div class="band band--top"></div>
    <span class="field field--contents" aria-label="Contents"><svg class="icon" width="18" height="18"><use href="#icon-contents"/></svg></span>
    <span class="field field--date" aria-label="Date"><svg class="icon" width="18" height="18"><use href="#icon-date"/></svg></span>
    <span class="slash slash--one">/</span>
    <span class="slash slash--two">/</span>
    <div class="band band--bottom"></div>
  </div>

  <div class="label label--copper">
    <span class="brand-name">LARDER</span>
    <div class="row row--contents"><span class="tab" aria-label="Contents"><svg class="icon"><use href="#icon-contents"/></svg></span><span class="dotted-line"></span></div>
    <div class="row row--date"><span class="tab" aria-label="Date"><svg class="icon"><use href="#icon-date"/></svg></span><span class="dotted-line"></span></div>
    <div class="row row--instructions"><span class="tab" aria-label="Instructions"><svg class="icon"><use href="#icon-instructions"/></svg></span><span class="dotted-line"></span></div>
  </div>

  <div class="label label--steel">
    <span class="brand-name">LARDER</span>
    <div class="row row--contents"><span class="tab" aria-label="Contents"><svg class="icon"><use href="#icon-contents"/></svg></span><span class="dotted-line"></span></div>
    <div class="row row--date"><span class="tab" aria-label="Date"><svg class="icon"><use href="#icon-date"/></svg></span><span class="dotted-line"></span></div>
    <div class="row row--instructions"><span class="tab" aria-label="Instructions"><svg class="icon"><use href="#icon-instructions"/></svg></span><span class="dotted-line"></span></div>
  </div>

  <div class="label label--teal">
    <span class="brand-name">LARDER</span>
    <div class="row row--contents"><span class="tab" aria-label="Contents"><svg class="icon"><use href="#icon-contents"/></svg></span><span class="dotted-line"></span></div>
    <div class="row row--date"><span class="tab" aria-label="Date"><svg class="icon"><use href="#icon-date"/></svg></span><span class="dotted-line"></span></div>
    <div class="row row--instructions"><span class="tab" aria-label="Instructions"><svg class="icon"><use href="#icon-instructions"/></svg></span><span class="dotted-line"></span></div>
  </div>

</body>
</html>
```